PROFESSIONAL MODERN REDESIGN OF CURRENT WEBSITE USING ALL SAME CONTENT

I need to redesign existing website using all existing exact content. Please do not leave anything missing. Use all content.

www.brightpathpromotionsgroup.biz

Target Market(s)

Small business owners, business to business, B2B

Industry/Entity Type

Direct Marketing

Number of Pages Required

5+ page

Colors

Designer to choose colors to be used in the design.

Requirements
Must have
• Must use exact same content as www.brightpathpromotionsgroup.biz
Nice to have
• I'd like this to be an easy to read professionally designed website with all modern elements...
Should not have
• Open

```html
<!DOCTYPE html>
<html lang="en">
<head>
<meta charset="utf-8">
<title>BrightPath Promotions Group – Website Sections</title>
<link href="https://fonts.googleapis.com/css2?family=Open+Sans:wght@300;400;600;700;800&display=swap" rel="stylesheet">
<style>
  :root{
    --brand-blue:#1a86d0;
    --brand-blue-dark:#1573b6;
    --ink:#1b1f24;
    --muted:#555c66;
    --white:#ffffff;
    --stage:#f4f9fd;
    --strip:#e9eef3;
  }
  *{box-sizing:border-box;margin:0;padding:0}
  html,body{width:1200px;height:676px;overflow:hidden}
  body{
    position:relative;
    background:radial-gradient(circle at 50% 50%, #fbfdff 0%, var(--stage) 60%, #e6f1fa 100%);
    font-family:"Open Sans", Arial, sans-serif;
    color:var(--ink);
  }
  .page{
    position:absolute;top:0;width:460px;height:676px;background:var(--white);
    box-shadow:0 0 28px rgba(26,134,208,.25);overflow:hidden;
  }
  .page--left{left:100px}
  .page--right{left:667px}
  .abs{position:absolute}
  .section-title{position:absolute;left:0;right:0;text-align:center;font-size:9.5px;font-weight:400;letter-spacing:.1px}
  .section-title b{font-weight:700}

  /* Left: areas */
  .areas{position:absolute;left:0;top:0;width:460px;height:399px;background:var(--brand-blue);color:var(--white)}
  .area{position:absolute;left:99px;width:300px}
  .area__num{position:absolute;left:0;top:-3px;font-size:13px;font-weight:700}
  .area__title{position:absolute;left:25px;top:0;font-size:6.2px;font-weight:700;white-space:nowrap}
  .area__text{position:absolute;left:25px;top:10px;width:140px;font-size:4.1px;line-height:6.4px;font-weight:400}
  .area__icon{position:absolute;left:214px;top:-4px;width:30px;height:30px}
  .cta-line{position:absolute;left:0;right:0;text-align:center;font-size:9px;font-weight:400}
  .cta-line b{font-weight:700}
  .btn{position:absolute;display:flex;align-items:center;justify-content:center;border-radius:10px;font-size:4.6px;font-weight:700;letter-spacing:.6px;text-transform:uppercase}
  .btn--outline{border:1px solid var(--white);color:var(--white)}
  .btn--solid{background:var(--brand-blue);color:var(--white)}

  /* Left: distribution */
  .channel{position:absolute;top:488px;width:70px}
  .channel__icon{width:26px;height:26px}
  .channel__title{margin-top:9px;font-size:6px;font-weight:700;line-height:8.5px}
  .channel__text{margin-top:3px;font-size:4.1px;line-height:6.4px;color:var(--muted)}
  .bottom-strip{position:absolute;left:0;top:670px;width:460px;height:6px;background:var(--strip)}

  /* Right: testimonials */
  .card{position:absolute;left:122px;top:50px;width:216px;height:149px;background:var(--white);border-radius:4px;box-shadow:0 3px 12px rgba(0,0,0,.12)}
  .card__quote{position:absolute;left:28px;top:26px;width:161px;font-size:3.9px;line-height:6.4px;color:var(--muted)}
  .card__rule{position:absolute;left:28px;top:104px;width:161px;height:1px;background:var(--brand-blue)}
  .card__avatar{position:absolute;left:31px;top:113px;width:20px;height:20px;border-radius:50%;background:linear-gradient(135deg,#b98a64,#6d4a35)}
  .card__name{position:absolute;left:59px;top:120px;font-size:4.3px;font-weight:700;color:var(--brand-blue)}
  .chev{position:absolute;width:8px;height:12px}

  .affiliate{position:absolute;left:0;top:300px;width:460px;height:167px;background:var(--brand-blue)}
  .affiliate__text{position:absolute;left:51px;top:50px;width:215px;font-size:8.6px;line-height:12.6px;color:var(--white);font-weight:400}
  .affiliate__photo{position:absolute;left:270px;top:341px;width:190px;height:154px;border-radius:16px 0 0 16px;
    background:linear-gradient(120deg,#e9eef2 0%,#cfd9e2 45%,#2b3a5a 75%,#1c2740 100%);box-shadow:0 4px 14px rgba(0,0,0,.2)}

  .client{position:absolute;top:580px;transform:translateX(-50%);font-size:8px;font-weight:700;color:var(--ink);white-space:nowrap}
</style>
</head>
<body>

<!-- Left page -->
<section class="page page--left">
  <div class="areas">
    <h2 class="section-title" style="top:36px;color:var(--white)">WE PLUG RIGHT INTO YOUR EXISTING ADVERTISING IN <b>4 MAJOR AREAS</b></h2>

    <div class="area" style="top:89px">
      <span class="area__num">1.</span>
      <h3 class="area__title">Boost Response Rates To Your Existing Ads</h3>
      <p class="area__text">Add a simple tagline to all your ads "contact us today and receive two nights in las vegas, no purchase necessary!"</p>
      <svg class="area__icon" viewBox="0 0 30 30" fill="none" stroke="#fff" stroke-width="1.4" stroke-linejoin="round"><path d="M15 3l3.6 7.6 8.2 1-6 5.7 1.5 8.2L15 21.5l-7.3 4 1.5-8.2-6-5.7 8.2-1z"/></svg>
    </div>

    <div class="area" style="top:142px">
      <span class="area__num">2.</span>
      <h3 class="area__title">Increase Repeat &amp; Referral Business</h3>
      <p class="area__text">You now have a reason to contact all of your past clients to remind them about your products &amp; services with a 7 night resort getaway to motivate them to buy again!</p>
      <svg class="area__icon" viewBox="0 0 30 30" fill="none" stroke="#fff" stroke-width="1.4"><rect x="4" y="14" width="4" height="13"/><rect x="13" y="9" width="4" height="18"/><rect x="22" y="3" width="4" height="24"/></svg>
    </div>

    <div class="area" style="top:195px">
      <span class="area__num">3.</span>
      <h3 class="area__title">Get More New Customers</h3>
      <p class="area__text">Now that you have generated a new lead go ahead and offer a higher valued incentive like our airfare plus hotel getaway persuade them to purchase today vs tomorrow!</p>
      <svg class="area__icon" viewBox="0 0 30 30" fill="none" stroke="#fff" stroke-width="1.4"><circle cx="12" cy="9" r="5"/><path d="M3 27c0-6 4-9 9-9s9 3 9 9"/><path d="M19 4.5a5 5 0 010 9"/><path d="M23 18c3 1 5 4 5 9"/></svg>
    </div>

    <div class="area" style="top:248px">
      <span class="area__num">4.</span>
      <h3 class="area__title">Boost Your Referral Business</h3>
      <p class="area__text">Offer a $100 wine voucher or even our two night bahama cruise to entice your customers to send you a referral and then watch your referral business soar!</p>
      <svg class="area__icon" viewBox="0 0 30 30" fill="none" stroke="#fff" stroke-width="1.4" stroke-linejoin="round"><path d="M3 20l9-9M6 10h7v7"/><path d="M10 27l17-17M19 4h9v9"/></svg>
    </div>

    <p class="cta-line" style="top:327px;color:var(--white)">Get quick <b>30 day</b> risk free trial</p>
    <a class="btn btn--outline" style="left:199px;top:349px;width:63px;height:17px">Sign up</a>
  </div>

  <h2 class="section-title" style="top:438px">EASY DISTRIBUTION OF <b>INCENTIVES</b></h2>

  <div class="channel" style="left:51px">
    <svg class="channel__icon" viewBox="0 0 26 26" fill="none" stroke="var(--brand-blue)" stroke-width="1.4"><rect x="7" y="1" width="12" height="7"/><rect x="1" y="8" width="24" height="11" rx="2"/><rect x="7" y="15" width="12" height="10"/></svg>
    <h3 class="channel__title">Print</h3>
    <p class="channel__text">Download PDF Certificates To Print And Physically Hand Them Out Or Mail Them To Your Customers.</p>
  </div>
  <div class="channel" style="left:148px">
    <svg class="channel__icon" viewBox="0 0 26 26" fill="none" stroke="var(--brand-blue)" stroke-width="1.4"><rect x="1" y="4" width="24" height="18"/><path d="M1 4l12 10 12-10"/></svg>
    <h3 class="channel__title">E-Mail</h3>
    <p class="channel__text">Email E-Certificates To Your Customers Individually And In Bulk With Just One Click.</p>
  </div>
  <div class="channel" style="left:245px">
    <svg class="channel__icon" viewBox="0 0 26 26" fill="none" stroke="var(--brand-blue)" stroke-width="1.4"><rect x="1" y="2" width="24" height="22"/><path d="M1 8h24"/><rect x="4" y="12" width="11" height="7"/><rect x="18" y="12" width="4" height="7"/></svg>
    <h3 class="channel__title">WEB banners or<br>API integration</h3>
    <p class="channel__text">Install Our HTML Web Banners On The Thank You Pages Of Your Website To Automate Distribution Of Our Incentives And If You Are Tech Savvy You Can Integrate Our NEW API Too!</p>
  </div>
  <div class="channel" style="left:342px">
    <svg class="channel__icon" viewBox="0 0 26 26" fill="none" stroke="var(--brand-blue)" stroke-width="1.4"><path d="M1 1h24v17H9l-6 6v-6H1z"/><rect x="6" y="8" width="3" height="3" fill="var(--brand-blue)"/><rect x="11.5" y="8" width="3" height="3" fill="var(--brand-blue)"/><rect x="17" y="8" width="3" height="3" fill="var(--brand-blue)"/></svg>
    <h3 class="channel__title">SMS/Text Messaging</h3>
    <p class="channel__text">Send Certificates Through Text Messaging With Just One Click With Our New SMS Feature With No Per Sms Fees!</p>
  </div>

  <a class="btn btn--solid" style="left:184px;top:623px;width:94px;height:16px">Click we will call you</a>
  <div class="bottom-strip"></div>
</section>

<!-- Right page -->
<section class="page page--right">
  <h2 class="section-title" style="top:17px"><b>CLIENT</b> TESTIMONIALS</h2>

  <svg class="chev" style="left:82px;top:117px" viewBox="0 0 8 12" fill="none" stroke="#c4c8cc" stroke-width="1.3"><path d="M7 1L2 6l5 5"/></svg>
  <svg class="chev" style="left:366px;top:117px" viewBox="0 0 8 12" fill="none" stroke="#c4c8cc" stroke-width="1.3"><path d="M1 1l5 5-5 5"/></svg>

  <article class="card">
    <p class="card__quote">i have been a customer with bppg for almost a year now, and i have been using the certificates for not only a "thank you" to close business deals, but as gifts to past clients as a "thank you" for their loyalty. i have had an overwhelming response from my clients that have used the certificates. the hotels stays are great and the restaurant certificates are a huge hit. some of my clients call me once a month to tell me about how great their dinner was at a new restaurant that they tried out with their certificate that i gave them. i am really impressed about how easy it is to redeem the certificates as well. i truly appreciate the incentive program and what i like about it the most is that it helps me differentiate myself from others in my industry.</p>
    <div class="card__rule"></div>
    <div class="card__avatar" role="img" aria-label="Client portrait"></div>
    <span class="card__name">MARK T.</span>
  </article>

  <p class="cta-line" style="top:234px">Get quick <b>30 day</b> risk free trial</p>
  <a class="btn btn--solid" style="left:198px;top:258px;width:61px;height:16px">Sign up</a>

  <div class="affiliate">
    <p class="affiliate__text">Know Any Businesses That Could Benefit Using Incentives To Bring In More Customers? Earn 40% RESIDUAL COMMISSIONS As An AFFILIATE!</p>
    <a class="btn btn--outline" style="left:51px;top:106px;width:63px;height:17px">Sign up</a>
  </div>
  <div class="affiliate__photo" role="img" aria-label="Photo of a businessman reviewing reports beside a monitor showing sales charts"></div>

  <h2 class="section-title" style="top:532px">OUR <b>CLIENTS</b></h2>
  <svg class="chev" style="left:64px;top:580px" viewBox="0 0 8 12" fill="none" stroke="#c4c8cc" stroke-width="1.3"><path d="M7 1L2 6l5 5"/></svg>
  <svg class="chev" style="left:388px;top:580px" viewBox="0 0 8 12" fill="none" stroke="#c4c8cc" stroke-width="1.3"><path d="M1 1l5 5-5 5"/></svg>
  <span class="client" style="left:117px">Harborline Realty</span>
  <span class="client" style="left:192px">ValueCrate</span>
  <span class="client" style="left:265px">Northway Motors</span>
  <span class="client" style="left:340px">SkyReach TV</span>

  <a class="btn btn--solid" style="left:198px;top:629px;width:65px;height:16px">Request a call</a>
</section>

</body>
</html>
```